QuadLantern--Help Us look fresh and new to companies, college students and college career centers!

We just designed a new logo and would like to freshen-up and make our business cards a bit more modern. Not crazy-modern like Velmont, but modern like metro-style and fresh like fruit. We use three logos with a combination of two colors each, and three colors total. We are looking for a single format to apply to three different cards/color schemes (green/blue to give out to companies, orange/green for students, and orange/blue for university career centers). Thanks everyone--looking forward to seeing your designs!!

Target Market(s)

Three styles: companies, college students/grads, college career centers

Industry/Entity Type

College

Contact Information for Business Card

Address: 5718 Harlow Street, Suite 412, Seattle, WA 98109. Need a spot for email address, web address (www.quadlantern.example), and phone numbers (main, direct, mobile). Don't open that website unless you want to lose your lunch--it is waaaay old and outdated. See this link instead, http://preview.mossgrovedev.example/QuadLantern/HiringTools, for our new website design in progress.

Font styles to use
Sans Serif

Requirements
Must have
• Please use the logos supplied. Would like text to be grey but printable, like a "light" type style that is metro-type with sans-serif. NOT black text. Modern. For inspiration, here's a link to our work-in-progress website we are planning to launch soon: http://preview.mossgrovedev.example/QuadLantern/HiringTools
Nice to have
• Would like to see something unique and different in a "metro" style. Clean and not cluttered.
Should not have
• No odd-sized cards

```html
<!DOCTYPE html>
<html lang="en">
<head>
<meta charset="utf-8">
<title>QuadLantern Business Card</title>
<link href="https://fonts.googleapis.com/css2?family=Open+Sans:wght@400;700&display=swap" rel="stylesheet">
<style>
  :root {
    --backdrop: #b7bcc4;
    --card-white: #f4f5f6;
    --brand-blue: #1a7fc4;
    --brand-green: #7cc142;
    --text-on-blue: #ffffff;
    --card-shadow: 0 12px 30px rgba(40, 50, 65, 0.25);
  }
  * { box-sizing: border-box; margin: 0; padding: 0; }
  html, body {
    width: 1200px;
    height: 866px;
    overflow: hidden;
  }
  body {
    background: var(--backdrop);
    font-family: "Open Sans", Arial, sans-serif;
    display: flex;
    align-items: center;
    justify-content: center;
    gap: 40px;
  }
  .card {
    position: relative;
    width: 540px;
    height: 310px;
    background: var(--card-white);
    box-shadow: var(--card-shadow);
    overflow: hidden;
  }
  .brand {
    display: flex;
    align-items: center;
    gap: 10px;
    color: var(--brand-green);
    font-weight: 700;
    letter-spacing: -0.5px;
  }
  .brand-dot {
    border-radius: 50%;
    background: var(--brand-blue);
    flex: none;
  }
  .card-front {
    display: flex;
    align-items: center;
    justify-content: center;
  }
  .card-front .brand { font-size: 50px; }
  .card-front .brand-dot { width: 34px; height: 34px; }

  .card-back .back-shapes {
    position: absolute;
    inset: 0;
    width: 100%;
    height: 100%;
  }
  .card-back .brand {
    position: absolute;
    left: 40px;
    top: 200px;
    font-size: 26px;
    gap: 7px;
  }
  .card-back .brand-dot { width: 18px; height: 18px; }

  .contact {
    position: absolute;
    right: 20px;
    top: 24px;
    text-align: right;
    color: var(--text-on-blue);
    font-size: 12px;
    line-height: 1.45;
  }
  .contact-name { font-weight: 700; font-size: 15px; }
  .contact-title { font-size: 14px; margin-bottom: 20px; }
  .contact-address { margin-bottom: 8px; }
  .contact-line {
    display: flex;
    justify-content: flex-end;
    align-items: center;
    gap: 5px;
  }
  .contact-line svg { width: 11px; height: 11px; fill: var(--text-on-blue); flex: none; }
</style>
</head>
<body>
  <section class="card card-front" aria-label="Card front">
    <div class="brand"><span class="brand-dot"></span>QuadLantern</div>
  </section>

  <section class="card card-back" aria-label="Card back">
    <svg class="back-shapes" viewBox="0 0 540 310" preserveAspectRatio="none" aria-hidden="true">
      <path d="M185,0 C285,40 335,150 330,310 L540,310 L540,0 Z" fill="var(--brand-blue)"/>
      <path d="M203,0 C297,42 345,150 341,310 L347,310 C353,150 307,38 217,0 Z" fill="#ffffff" opacity="0.85"/>
      <path d="M318,120 C356,180 362,245 346,310 L374,310 C380,245 364,180 318,120 Z" fill="var(--brand-green)"/>
    </svg>

    <div class="brand"><span class="brand-dot"></span>QuadLantern</div>

    <div class="contact">
      <p class="contact-name">Maren Holt-Avery</p>
      <p class="contact-title">Consultant</p>
      <p class="contact-address">412 Harlow Street,<br>Seattle WA</p>
      <p class="contact-line">206 555 0147
        <svg viewBox="0 0 24 24"><path d="M6.6 10.8a15 15 0 0 0 6.6 6.6l2.2-2.2a1 1 0 0 1 1-.25 11.4 11.4 0 0 0 3.6.57 1 1 0 0 1 1 1V20a1 1 0 0 1-1 1A17 17 0 0 1 3 4a1 1 0 0 1 1-1h3.5a1 1 0 0 1 1 1c0 1.25.2 2.45.57 3.57a1 1 0 0 1-.25 1z"/></svg>
      </p>
      <p class="contact-line">206 555 0148
        <svg viewBox="0 0 24 24"><path d="M5 3h11v5h3v13H5zM8 6v3h5V6zm0 6v2h2v-2zm4 0v2h2v-2zm-4 4v2h2v-2zm4 0v2h2v-2z"/></svg>
      </p>
      <p class="contact-line">hello@quadlantern.example
        <svg viewBox="0 0 24 24"><path d="M2 5h20v14H2zm2 2v.5l8 5 8-5V7l-8 5z"/></svg>
      </p>
      <p class="contact-line">www.quadlantern.example</p>
    </div>
  </section>
</body>
</html>
```